Rising Paths Web Design

I am starting a new company that will provide LIFE COACHING services - I have tried to design a website, but it's too complicated. Right now, it's just me - I'm the only person that will provide services through the website - I have used artmarket to purchase a logo (see below). I want to be able to update the website myself, but need a template - basic design. Because I am not technologically savvy enough to explain in words - I basically want to have a website that will provide basic information about my services (coaching), a page about me and my background, hopefully scheduling possibilities, and testimonials — also a page for writing/blogs. I bought a website through NetHarbor - so when I have a template, I guess I”d use that - but maybe I’ll need to work with a designer to actually get it up on the internet. I have a head shot that I’ll upload, too.
Target Market(s)
Clients from the independent (private school) world - teachers, administrators
Number of Pages Required
4 page
Look and feel
Each slider illustrates characteristics of the customer's brand and the style your logo design should communicate.

```html
<!DOCTYPE html>
<html lang="en">
<head>
<meta charset="utf-8">
<title>Rising Paths Coaching</title>
<link href="https://fonts.googleapis.com/css2?family=Crimson+Text:wght@400;600&family=Roboto:wght@400;500&display=swap" rel="stylesheet">
<style>
:root{
  --teal:#13a89a;
  --ink:#2b2b2b;
  --muted:#666;
  --light:#f3f3f3;
  --forest:#1f4a2a;
  --footer:#0d2b2b;
  --footer-base:#0a1f20;
  --white:#fff;
}
*{box-sizing:border-box;margin:0;padding:0}
html,body{width:1200px;height:3613px;overflow:hidden}
body{position:relative;font-family:"Crimson Text",serif;color:var(--ink);background:var(--white)}
.abs{position:absolute}
.btn{position:absolute;background:var(--teal);color:var(--white);font:600 12px "Crimson Text",serif;letter-spacing:.5px;text-transform:uppercase;display:flex;align-items:center;justify-content:center}
.center{left:0;width:1200px;text-align:center}

/* header */
.header{top:0;left:0;width:1200px;height:118px;background:var(--white)}
.brand{left:87px;top:20px;display:flex;align-items:center;gap:10px}
.brand-ring{width:74px;height:74px;border:2px solid var(--teal);border-radius:50%}
.brand-name{font:400 17px "Crimson Text",serif;color:var(--footer);letter-spacing:.5px;text-transform:uppercase}
.nav{top:56px;left:0;width:1200px;font:400 11.5px "Crimson Text",serif;text-transform:uppercase;letter-spacing:.4px;color:#333}
.nav span{position:absolute}
.book{left:990px;top:49px;width:125px;height:28px;font-size:11px}

/* hero */
.hero{top:118px;left:0;width:1200px;height:443px;background:linear-gradient(180deg,#5d6670 0%,#4a5058 45%,#6c5a3a 85%,#3b3a36 100%)}
.hero-name{top:210px;font-size:21px;color:#e6e1d8}
.hero-title{top:258px;font-size:51px;line-height:61px;color:var(--white)}
.hero-btn{left:530px;top:416px;width:140px;height:45px}

/* about */
.portrait{left:125px;top:669px;width:326px;height:433px;background:linear-gradient(160deg,#d9d6cf,#b7ad9c 60%,#8f8576)}
.about-title{left:519px;top:708px;font-size:32px;color:#333}
.about-title em{font-style:normal;color:var(--teal)}
.about-copy{left:519px;top:776px;width:560px;font-size:14px;line-height:20.5px;color:#555}
.about-copy p{margin-bottom:7px}
.about-btn{left:519px;top:1025px;width:138px;height:45px}

/* services */
.services{top:1224px;left:0;width:1200px;height:607px;background:linear-gradient(180deg,#6a6b72 0%,#8d7d6d 18%,#4c6a72 30%,#8a8e8a 60%,#a79a87 100%)}
.section-title{font-size:41px;color:var(--white)}
.services-title{top:1300px}
.card{position:absolute;top:1412px;width:231px;height:319px;background:var(--white)}
.card-img{height:189px}
.card-label{height:130px;display:flex;align-items:center;justify-content:center;text-align:center;padding:0 24px;font:600 16px/22px "Crimson Text",serif;color:#333}
.dots{position:absolute;display:flex;gap:9px}
.dots i{width:8px;height:8px;border-radius:50%;border:1.5px solid var(--ink)}
.dots i.on{background:var(--ink)}
.dots.light i{border-color:var(--white)}
.dots.light i.on{background:var(--white)}

/* events */
.events{top:1831px;left:0;width:1200px;height:676px;background:var(--light)}
.events-title{top:1915px;font-size:33px;font-weight:600;color:var(--teal)}
.rule{position:absolute;height:3px;width:58px;background:var(--teal);left:571px}
.post{position:absolute;left:100px;width:574px;height:186px;background:var(--white)}
.post-img{position:absolute;left:0;top:0;width:258px;height:186px}
.post-body{position:absolute;left:284px;top:20px;width:270px}
.post-body h3{font-size:19px;line-height:26px;font-weight:600;color:#333}
.meta{font-size:10px;color:#666;text-transform:uppercase;margin:6px 0 12px}
.meta b{font-weight:400;color:var(--teal)}
.post-body p{font-size:14px;line-height:22px;color:#666}
.more{font-size:10.5px;color:#999;text-decoration:underline;text-transform:uppercase}
.event{position:absolute;left:701px;width:399px;height:117px;background:var(--white)}
.day{position:absolute;left:0;width:118px;top:18px;text-align:center;font-size:42px;line-height:44px;color:var(--teal)}
.month{position:absolute;left:0;width:118px;top:68px;text-align:center;font-size:12px;letter-spacing:2px;color:var(--teal)}
.event-body{position:absolute;left:120px;top:20px}
.event-body h3{font-size:18px;font-weight:600;color:#333}
.event-body .meta{margin:4px 0 14px}

/* stories */
.stories{top:2507px;left:0;width:1200px;height:472px;background:radial-gradient(ellipse at 65% 40%,#3e6a3c 0%,#284f2c 40%,#173a22 100%)}
.stories-title{top:2600px;font-size:33px;font-weight:600}
.avatar{position:absolute;width:120px;height:120px;border-radius:50%;border:3px solid var(--white);background:linear-gradient(160deg,#e2dcd4,#b8a89a)}
.quote{position:absolute;width:350px;color:var(--white)}
.quote .lead{color:var(--teal);font-size:16px;margin-bottom:10px}
.quote .lead span{font-size:26px;vertical-align:-8px;margin-right:12px;font-weight:600}
.quote p{font-size:16px;line-height:26px}
.quote .who{font-weight:600;font-size:15px;margin-top:4px}
.quote .role{font-size:12.5px}

/* callback */
.cb-title{top:3025px;font-size:32px;color:#333}
.cb-sub{top:3084px;font-size:14px;line-height:23px;color:#555}
.field{position:absolute;top:3171px;width:230px;height:38px;border:1px solid #e2e2e2;font:400 11.5px "Roboto",sans-serif;color:#666;padding:12px 20px}
.submit{left:903px;top:3171px;width:146px;height:38px;font-family:"Roboto",sans-serif;font-weight:500;font-size:11px}

/* footer */
.footer{top:3262px;left:0;width:1200px;height:308px;background:var(--footer)}
.footer-base{top:3570px;left:0;width:1200px;height:43px;background:var(--footer-base)}
.f-brand{left:130px;top:3302px;display:flex;align-items:center;gap:8px}
.f-brand .brand-ring{width:88px;height:88px;position:absolute;left:0;top:0;border-color:var(--teal)}
.f-brand .brand-name{color:var(--white);position:relative;left:6px;top:30px;font-size:15px}
.f-contact{left:130px;font:400 11.5px "Roboto",sans-serif;color:#cfd8d8;display:flex;align-items:center;gap:12px}
.f-contact svg{width:12px;height:12px;fill:#cfd8d8}
.social{position:absolute;top:3496px;width:34px;height:34px;border-radius:50%;background:#1e3c3c}
.social.on{background:var(--teal)}
.f-head{font:500 11.5px "Roboto",sans-serif;color:var(--white);text-transform:uppercase;top:3356px}
.f-link{font:400 11.5px "Roboto",sans-serif;color:#cfd8d8}
.copy{top:3584px;left:130px;font:400 11px "Roboto",sans-serif;color:#7f9090}
.legal{top:3584px;right:91px;font:400 11px "Roboto",sans-serif;color:var(--teal)}
.legal span{color:#7f9090;margin:0 6px}
</style>
</head>
<body>

<header class="abs header">
  <div class="abs brand"><div class="brand-ring"></div><div class="brand-name">Rising Paths</div></div>
  <nav class="abs nav">
    <span style="left:319px">Home</span>
    <span style="left:395px">About Me</span>
    <span style="left:493px">Services</span>
    <span style="left:588px">Events</span>
    <span style="left:689px">Testimonials</span>
    <span style="left:818px">Blog</span>
    <span style="left:890px">Contact</span>
  </nav>
  <div class="btn book">Book a Session</div>
</header>

<section class="abs hero" role="img" aria-label="City skyline of tall office towers at golden hour"></section>
<div class="abs center hero-name">Clara Whitmore Dane</div>
<h1 class="abs center hero-title" style="font-weight:400">Success is a Progressive Idea<br>Worth Pursuing</h1>
<div class="btn hero-btn">Learn More</div>

<div class="abs portrait" role="img" aria-label="Head shot of the coach in a kitchen"></div>
<h2 class="abs about-title" style="font-weight:400">Hola! I am <em>Clara Whitmore Dane</em></h2>
<div class="abs about-copy">
  <p>Lorem ipsum dolor sit amet, consectetur adipiscing elit, sed do eiusmod tempor incididunt ut labore et dolore magna aliqua. Quis ipsum suspendisse ultrices gravida. Risus commodo viverra maecenas accumsan lacus vel facilisis. Lorem ipsum dolor sit amet, consectetur adipiscing elit, sed do eiusmod tempor incididunt ut labore et dolore magna aliqua. Quis ipsum suspendisse ultrices gravida. Risus commodo viverra maecenas accumsan lacus vel facilisis.</p>
  <p>Quis ipsum suspendisse ultrices gravida. Risus commodo viverra maecenas accumsan lacus vel facilisis. Lorem ipsum dolor sit amet, consectetur adipiscing elit, sed do eiusmod tempor incididunt ut labore et dolore magna aliqua. Quis ipsum suspendisse ultrices gravida. Risus commodo viverra maecenas accumsan lacus vel facilisis.</p>
</div>
<div class="btn about-btn">Learn More</div>

<section class="abs services" role="img" aria-label="Beach at sunset with ocean waves"></section>
<h2 class="abs center section-title services-title" style="font-weight:400">My Services</h2>
<div class="card" style="left:98px"><div class="card-img" role="img" aria-label="Classroom with chalkboards" style="background:linear-gradient(160deg,#6b6a4e,#3e4a3c)"></div><div class="card-label">How to become a Biomedical Engineer</div></div>
<div class="card" style="left:356px"><div class="card-img" role="img" aria-label="Large audience in an auditorium" style="background:linear-gradient(160deg,#b9b0a4,#6c6258)"></div><div class="card-label">MS in Computer Science Courses in the USA</div></div>
<div class="card" style="left:613px"><div class="card-img" role="img" aria-label="Students talking in a colourful gallery" style="background:linear-gradient(160deg,#9a4a3c,#3a3036)"></div><div class="card-label">The study of the human mind.</div></div>
<div class="card" style="left:870px"><div class="card-img" role="img" aria-label="Group gathered in a meeting room" style="background:linear-gradient(160deg,#7a7a78,#4a4642)"></div><div class="card-label">The study of information technology.</div></div>
<div class="dots" style="left:578px;top:1776px"><i></i><i class="on"></i><i></i></div>

<section class="abs events"></section>
<h2 class="abs center events-title">Events &amp; Blogs</h2>
<div class="rule" style="top:1976px"></div>

<article class="post" style="top:2022px">
  <div class="post-img" role="img" aria-label="Wall of colourful paper strips with handwritten values" style="background:linear-gradient(150deg,#e9e2c6,#9cc7d8 55%,#d8d4cc)"></div>
  <div class="post-body">
    <h3>Use These Four Guiding Princi-ples in Difficult Conversations</h3>
    <div class="meta">Posted 05.17.2017 &nbsp;|&nbsp; <b>By Lena Hart</b></div>
    <p>Don't be distracted by criticism. Remember the only taste of success some people.</p>
  </div>
</article>
<article class="post" style="top:2228px">
  <div class="post-img" role="img" aria-label="Information table at a school fair" style="background:linear-gradient(160deg,#6d6a68,#1e4a44 70%)"></div>
  <div class="post-body">
    <h3>Excellent job fair at Westbrook!</h3>
    <div class="meta">Posted 05.17.2017 &nbsp;|&nbsp; <b>By Lena Hart</b></div>
    <p>Don't be distracted by criticism. Remember the only taste of success some people.</p>
    <div class="more" style="margin-top:10px">View Details</div>
  </div>
</article>

<div class="event" style="top:2022px"><div class="day">04</div><div class="month">DEC</div><div class="event-body"><h3>Speaking &amp; Workshops</h3><div class="meta">Newyork, US &nbsp;&nbsp; 10:00 PM – 06:00 AM</div><div class="more">View Details</div></div></div>
<div class="event" style="top:2159px"><div class="day">22</div><div class="month">JUN</div><div class="event-body"><h3>Are You An Effective Leader?</h3><div class="meta">Newyork, US &nbsp;&nbsp; 10:00 PM – 06:00 AM</div><div class="more">View Details</div></div></div>
<div class="event" style="top:2295px"><div class="day">15</div><div class="month">AUG</div><div class="event-body"><h3>Is There an Author Inside You?</h3><div class="meta">Newyork, US &nbsp;&nbsp; 10:00 PM – 06:00 AM</div><div class="more">View Details</div></div></div>

<section class="abs stories" role="img" aria-label="Dark green leafy garden backdrop"></section>
<h2 class="abs center section-title stories-title">Success Stories</h2>
<div class="rule" style="top:2663px"></div>
<div class="avatar" style="left:100px;top:2743px" role="img" aria-label="Client portrait"></div>
<div class="quote" style="left:250px;top:2705px">
  <div class="lead"><span>“</span>i have successfully completed</div>
  <p>Even though I am a seasoned business owner myself, I am sure that there’s always room for growth, inspiration, and new ideas.”</p>
  <div class="who">Owen Marsh</div><div class="role">CEO Fernlight Studio</div>
</div>
<div class="avatar" style="left:616px;top:2743px" role="img" aria-label="Client portrait"></div>
<div class="quote" style="left:761px;top:2705px;width:360px">
  <div class="lead"><span>“</span>i have successfully completed</div>
  <p>”Coaching has provided a common language that is gaining popularity in the workplace as it creates new learning and sets people up for success. ”</p>
  <div class="who">Nadia Brooks</div><div class="role">Creative Director</div>
</div>
<div class="dots light" style="left:564px;top:2925px"><i></i><i class="on"></i><i></i></div>

<h2 class="abs center cb-title" style="font-weight:400">Request a Call Back</h2>
<p class="abs center cb-sub">You are one step closer to creating a healthier and happier<br>life for yourself, as well as those around you. Get started on your application below.</p>
<div class="field" style="left:182px">First Name</div>
<div class="field" style="left:422px">Phone Number</div>
<div class="field" style="left:662px">Your Email</div>
<div class="btn submit">Submit</div>

<footer class="abs footer"></footer>
<div class="abs f-brand" style="width:160px;height:90px"><div class="brand-ring"></div><div class="brand-name">Rising Paths</div></div>
<div class="abs f-contact" style="top:3413px"><svg viewBox="0 0 24 24"><path d="M6.6 10.8a15 15 0 0 0 6.6 6.6l2.2-2.2c.3-.3.7-.4 1-.2 1.1.4 2.3.6 3.6.6.6 0 1 .4 1 1V20c0 .6-.4 1-1 1A17 17 0 0 1 3 4c0-.6.4-1 1-1h3.5c.6 0 1 .4 1 1 0 1.3.2 2.5.6 3.6.1.3 0 .7-.2 1z"/></svg>+1 800 555 0142</div>
<div class="abs f-contact" style="top:3439px"><svg viewBox="0 0 24 24"><path d="M2 5h20v14H2z M2 5l10 8 10-8" fill="none" stroke="#cfd8d8" stroke-width="2"/></svg>hello@risingpaths.example</div>
<div class="abs f-contact" style="top:3464px"><svg viewBox="0 0 24 24"><path d="M12 2a7 7 0 0 0-7 7c0 5 7 13 7 13s7-8 7-13a7 7 0 0 0-7-7zm0 9.5A2.5 2.5 0 1 1 12 6.5a2.5 2.5 0 0 1 0 5z"/></svg>12 Alder Lane 48/3 Riverton, US</div>
<div class="social" style="left:129px"></div>
<div class="social on" style="left:171px"></div>
<div class="social" style="left:214px"></div>
<div class="social" style="left:256px"></div>

<div class="abs f-head" style="left:471px">Featured Courses</div>
<div class="abs f-link" style="left:471px;top:3397px">Starting Soon</div>
<div class="abs f-link" style="left:471px;top:3428px">Just Added</div>
<div class="abs f-link" style="left:471px;top:3458px">Most Viewed</div>
<div class="abs f-link" style="left:471px;top:3489px">Top Paid</div>

<div class="abs f-head" style="left:643px">Categories</div>
<div class="abs f-link" style="left:643px;top:3397px">Arts &amp; Design</div>
<div class="abs f-link" style="left:643px;top:3428px">Business</div>
<div class="abs f-link" style="left:643px;top:3458px">Computer Science</div>
<div class="abs f-link" style="left:643px;top:3489px">Data Science</div>

<div class="abs f-head" style="left:813px">Useful Links</div>
<div class="abs f-link" style="left:813px;top:3386px">Home</div>
<div class="abs f-link" style="left:813px;top:3417px">About Me</div>
<div class="abs f-link" style="left:813px;top:3448px">Services</div>
<div class="abs f-link" style="left:813px;top:3478px">Testimonial</div>
<div class="abs f-link" style="left:959px;top:3383px">Contact</div>
<div class="abs f-link" style="left:959px;top:3425px">Blog</div>

<div class="abs footer-base"></div>
<div class="abs copy">© 2022 Rising Paths.. All rights reserved.</div>
<div class="abs legal">Privacy<span>|</span>Terms<span>|</span>Sitemap<span>|</span>Help</div>

</body>
</html>
```